Business Card Project

We are a small consulting firm. You can experiment with any design.
Must have:
1) Company name - OLUNDEX International
2) Company slogan - simple solutions for complex problems
3) Name/Title/Phone/Email/WWW/ - use anything you like as an example.

Industry/Entity Type

Business

```html
<!DOCTYPE html>
<html lang="en">
<head>
<meta charset="utf-8">
<title>OLUNDEX International – Business Card</title>
<link rel="stylesheet" href="https://fonts.googleapis.com/css2?family=Open+Sans:wght@400;600&display=swap">
<style>
  :root {
    --backdrop: #e9e6e2;
    --card-dark: #1c1e23;
    --card-light: #ffffff;
    --brand-blue: #2a9fdb;
    --text-grey: #7a7c80;
    --slogan-grey: #b9bcc1;
    --logo-light: #e6e7ea;
    --logo-dark: #55575c;
  }
  * { margin: 0; padding: 0; box-sizing: border-box; }
  html, body { width: 1200px; height: 684px; overflow: hidden; }
  body {
    position: relative;
    background: var(--backdrop);
    font-family: "Open Sans", Arial, sans-serif;
  }
  .card {
    position: absolute;
    top: 99px;
    width: 302px;
    height: 494px;
    box-shadow: 0 2px 6px rgba(0,0,0,0.25);
  }
  .card--front { left: 243px; background: var(--card-dark); }
  .card--back { left: 660px; background: var(--card-light); }

  .brand {
    position: absolute;
    display: flex;
    align-items: center;
    gap: 12px;
    font-weight: 400;
  }
  .brand__dot {
    width: 34px; height: 34px;
    border-radius: 50%;
    background: var(--brand-blue);
    flex: none;
  }
  .brand__name { line-height: 1; }
  .brand__word { display: block; font-size: 30px; letter-spacing: 1px; }
  .brand__sub { display: block; font-size: 11px; letter-spacing: 4.6px; margin-top: 4px; }
  .card--front .brand { left: 28px; top: 180px; color: var(--logo-light); }
  .card--back .brand { left: 34px; top: 58px; color: var(--logo-dark); }

  .slogan {
    position: absolute;
    left: 0; right: 0; bottom: 25px;
    text-align: center;
    font-size: 13px;
    letter-spacing: 0.4px;
    color: var(--slogan-grey);
  }

  .person {
    position: absolute;
    left: 0; right: 0; top: 180px;
    text-align: center;
  }
  .person__name {
    font-size: 22px;
    letter-spacing: 0.8px;
    color: var(--brand-blue);
    line-height: 28px;
  }
  .person__title {
    font-size: 15px;
    color: var(--text-grey);
    margin-top: 3px;
  }

  .contacts {
    position: absolute;
    left: 70px; top: 322px;
    list-style: none;
  }
  .contacts__item {
    display: flex;
    align-items: center;
    gap: 10px;
    height: 27px;
    font-size: 13px;
    color: var(--text-grey);
  }
  .contacts__icon {
    width: 13px; height: 13px;
    border-radius: 50%;
    background: var(--brand-blue);
    color: #fff;
    font-size: 7px;
    font-weight: 600;
    display: flex; align-items: center; justify-content: center;
    flex: none;
  }
</style>
</head>
<body>
  <section class="card card--front" aria-label="Card front">
    <div class="brand">
      <span class="brand__dot"></span>
      <span class="brand__name">
        <span class="brand__word">OLUNDEX</span>
        <span class="brand__sub">INTERNATIONAL</span>
      </span>
    </div>
    <p class="slogan">Simple Solutions For Complex Problems</p>
  </section>

  <section class="card card--back" aria-label="Card back">
    <div class="brand">
      <span class="brand__dot"></span>
      <span class="brand__name">
        <span class="brand__word">OLUNDEX</span>
        <span class="brand__sub">INTERNATIONAL</span>
      </span>
    </div>
    <div class="person">
      <h1 class="person__name">MARCO VELLAN</h1>
      <p class="person__title">Creative Director</p>
    </div>
    <ul class="contacts">
      <li class="contacts__item"><span class="contacts__icon">A</span>88 Calle Brisa Norte</li>
      <li class="contacts__item"><span class="contacts__icon">E</span>email@yourdomain.com</li>
      <li class="contacts__item"><span class="contacts__icon">M</span>0123 456 789</li>
      <li class="contacts__item"><span class="contacts__icon">W</span>www.yourdomain.com</li>
    </ul>
  </section>
</body>
</html>
```